Golf Tournament Sponsorship Sign

We need to create a 18" x 24" poster sign that will be an advertisement on a tee box at a golf tournament. We are a Managed IT Services company. We would like to include our logo, a quick overview of our services (Managed IT Services, Cybersecurity, IT Automation, Quarnelle 480). We would like to leave a spot for a QR code with "Chance to win a free round of golf by scanning..."

```html
<!DOCTYPE html>
<html lang="en">
<head>
<meta charset="utf-8">
<title>Nexaline – Golf Tournament Tee Sign</title>
<link href="https://fonts.googleapis.com/css2?family=Bebas+Neue&family=Poppins:wght@400;600;700&display=swap" rel="stylesheet">
<style>
  :root {
    --backdrop: #212121;
    --turf-light: #8fcf5a;
    --turf-mid: #5aa632;
    --turf-deep: #3f8a22;
    --navy: #142c63;
    --band-blue: #1d609c;
    --brand-blue: #1f5fd0;
    --ink: #111111;
    --white: #ffffff;
    --qr-frame: #2b8a94;
    --qr-fill: rgba(240, 246, 236, 0.9);
  }
  * { margin: 0; padding: 0; box-sizing: border-box; }
  html, body {
    width: 1200px; height: 1200px; overflow: hidden;
    background: var(--backdrop);
  }
  .sign {
    position: absolute; left: 0; top: 150px;
    width: 1200px; height: 900px; overflow: hidden;
  }
  .course-photo {
    position: absolute; inset: 0 0 180px 0;
    background:
      radial-gradient(ellipse at 75% 20%, rgba(240,250,220,0.55), transparent 55%),
      radial-gradient(ellipse at 30% 30%, rgba(30,60,20,0.35), transparent 40%),
      linear-gradient(180deg, var(--turf-light) 0%, var(--turf-mid) 55%, var(--turf-deep) 100%);
  }
  .brand {
    position: absolute; left: 727px; top: 128px;
    display: flex; flex-direction: column; align-items: flex-start;
  }
  .brand-name {
    display: flex; align-items: center; gap: 14px;
    font-family: 'Poppins', sans-serif; font-weight: 700;
    font-size: 56px; line-height: 1; letter-spacing: 10px;
    color: var(--ink);
  }
  .brand-mark {
    width: 34px; height: 34px; background: var(--brand-blue);
  }
  .brand-tagline {
    margin-top: 8px; margin-left: 48px;
    font-family: 'Poppins', sans-serif; font-weight: 400;
    font-size: 24px; line-height: 1; letter-spacing: 5.5px; color: var(--ink);
  }
  .headline {
    position: absolute; left: 73px; top: 345px;
    font-family: 'Bebas Neue', sans-serif; font-weight: 400;
    font-size: 100px; line-height: 90px; letter-spacing: 1.5px;
    color: var(--white);
  }
  .qr-spot {
    position: absolute; left: 739px; top: 289px;
    width: 385px; height: 362px;
    border: 5px solid var(--qr-frame); border-radius: 28px;
    background: var(--qr-fill);
  }
  .service-band {
    position: absolute; left: 0; top: 640px; width: 1200px; height: 260px;
  }
  .services {
    position: absolute; left: 237px; top: 742px;
    font-family: 'Poppins', sans-serif; font-weight: 600;
    font-size: 41px; line-height: 56px; letter-spacing: 2.4px;
    color: var(--white); white-space: nowrap;
  }
</style>
</head>
<body>
  <main class="sign">
    <div class="course-photo" role="img" aria-label="Close-up photo of a golf club head next to a golf ball on a green fairway"></div>

    <svg class="service-band" viewBox="0 0 1200 260" preserveAspectRatio="none" aria-hidden="true">
      <defs>
        <linearGradient id="bandFill" x1="0" x2="1" y1="0" y2="0">
          <stop offset="0" stop-color="#142c63"/>
          <stop offset="0.5" stop-color="#1d609c"/>
          <stop offset="1" stop-color="#142c63"/>
        </linearGradient>
      </defs>
      <path d="M0 0 Q600 110 1200 10 L1200 260 L0 260 Z" fill="url(#bandFill)"/>
    </svg>

    <div class="brand">
      <div class="brand-name"><span class="brand-mark"></span>NEXALINE</div>
      <div class="brand-tagline">TEE OFF WITH TECH</div>
    </div>

    <h1 class="headline">Chance to win a<br>free round of golf<br>by scanning...</h1>

    <div class="qr-spot" aria-label="Space reserved for QR code"></div>

    <p class="services">Managed IT Services, Cybersecurity,<br>IT Automation, Quarnelle 480</p>
  </main>
</body>
</html>
```